Hi, We are global cloud printer looking to start a ad print run, we require full and half page print ad's designed with the following dimensions

Full page dimensions:

Image area: 345 mm in height x 260 mm (6 columns) in width
Trim area: 368 mm in height x 280 mm (6 columns) in width
Bleed area: 371 mm in height x 283 mm (6 columns) in width

Half-page dimensions:
270 mm in height x 172 mm (4 columns) in width

We want a minimalistic ad that really stands out from the crowd, with a full page we want it to make an impact and drive people towards our site.

The site is www.plaventro.com , we would like to match the look and feel but would like the wow factor so our open to all concepts.

We would like the following tagline incorporated in the Ad The cloud you've been waiting for, might be closer than you think.

```html
<!DOCTYPE html>
<html lang="en">
<head>
<meta charset="utf-8">
<title>Plaventro print ads – full and half page</title>
<link href="https://fonts.googleapis.com/css2?family=Nunito:wght@400;600;700;800&display=swap" rel="stylesheet">
<style>
:root{
  --green:#7fbf00;
  --green-light:#c4e86c;
  --green-label:#8cc63f;
  --slate:#475864;
  --slate-dark:#3a4853;
  --white:#ffffff;
  --ink:#111111;
  --cloud-blue:#bfe0f5;
  --server-grey:#d9dde0;
}
*{margin:0;padding:0;box-sizing:border-box}
html,body{width:1200px;height:1072px;overflow:hidden;background:var(--white)}
body{position:relative;font-family:"Nunito",sans-serif;color:var(--white)}

.size-label{position:absolute;font-weight:800;font-size:19px;color:var(--ink);transform:translateX(-50%);letter-spacing:.2px}
.size-label--full{left:387px;top:88px}
.size-label--half{left:943px;top:311px}

.ad{position:absolute;overflow:hidden;background:radial-gradient(ellipse 60% 45% at 42% 32%,var(--green-light) 0%,var(--green) 70%);border:1px solid #9aa}
.ad--full{left:69px;top:131px;width:630px;height:826px}
.ad--half{left:755px;top:354px;width:353px;height:598px}

.ad__art{position:absolute;border-radius:40px 40px 30px 30px;background:linear-gradient(180deg,var(--server-grey) 0%,var(--cloud-blue) 60%,#9fd0f0 100%);opacity:.95}
.ad__shadow{position:absolute;border-radius:50%;background:rgba(60,110,0,.45);filter:blur(2px)}
.ad__arm{position:absolute;background:linear-gradient(180deg,#ff3b1a 0%,#ff3b1a 30%,var(--white) 31%,var(--white) 52%,var(--slate) 53%,var(--slate-dark) 100%);border-radius:8px 8px 0 0}
.ad__link{position:absolute;overflow:visible}

.ad__heading{position:absolute;font-weight:700;line-height:1.35}
.ad__intro{position:absolute;font-weight:400;line-height:1.75}
.ad__points{position:absolute;list-style:none;font-weight:700}
.ad__points li::before{content:"• "}

.badge{position:absolute;overflow:visible}

.footer{position:absolute;left:0;bottom:0;width:100%;background:var(--slate)}
.footer__contacts{position:absolute;font-weight:600}
.footer__row{display:flex;align-items:baseline;white-space:nowrap}
.footer__label{color:var(--green-label);font-weight:400;text-align:right}
.footer__value{color:var(--white);font-weight:700}
.footer__divider{position:absolute;top:8px;bottom:8px;width:1px;background:#8a99a3}
.footer__brand{position:absolute}
.footer__regions{font-weight:800;letter-spacing:1.2px;white-space:nowrap}
.brand{display:flex;align-items:center}
.brand__mark{background:var(--green);flex:none}
.brand__text{display:flex;flex-direction:column}
.brand__name{font-weight:800;color:var(--white);line-height:1}
.brand__tagline{font-weight:700;text-transform:uppercase;letter-spacing:.6px;line-height:1.25;color:var(--white)}
.footer__url{font-weight:800;white-space:nowrap}

/* full page sizing */
.ad--full .ad__art{left:32px;top:22px;width:392px;height:345px}
.ad--full .ad__shadow{left:60px;top:368px;width:350px;height:12px}
.ad--full .ad__arm{left:504px;top:405px;width:126px;height:296px}
.ad--full .ad__link{left:337px;top:68px;width:220px;height:345px}
.ad--full .ad__heading{left:55px;top:440px;font-size:20px}
.ad--full .ad__intro{left:55px;top:494px;width:330px;font-size:10.5px}
.ad--full .ad__points{left:55px;top:558px;font-size:14.5px;line-height:22.5px}
.ad--full .badge{left:376px;top:522px;width:142px;height:142px}
.ad--full .footer{height:125px}
.ad--full .footer__contacts{left:55px;top:20px;font-size:13px;line-height:24px}
.ad--full .footer__label{width:90px;margin-right:4px}
.ad--full .footer__label--spaced{letter-spacing:6px}
.ad--full .footer__divider{left:340px}
.ad--full .footer__brand{left:366px;top:12px}
.ad--full .footer__regions{font-size:7px;margin-bottom:14px}
.ad--full .brand__mark{width:38px;height:38px;margin-right:12px}
.ad--full .brand__name{font-size:29px}
.ad--full .brand__tagline{font-size:5.2px;margin-top:3px}
.ad--full .footer__url{font-size:10px;letter-spacing:5px;margin-top:16px}

/* half page sizing */
.ad--half .ad__art{left:19px;top:54px;width:223px;height:190px;border-radius:24px 24px 18px 18px}
.ad--half .ad__shadow{left:35px;top:250px;width:200px;height:7px}
.ad--half .ad__arm{left:282px;top:353px;width:71px;height:169px;border-radius:5px 5px 0 0}
.ad--half .ad__link{left:189px;top:78px;width:125px;height:275px}
.ad--half .ad__heading{left:27px;top:283px;font-size:14px}
.ad--half .ad__intro{left:27px;top:360px;width:138px;font-size:6.5px;line-height:1.8}
.ad--half .ad__points{left:27px;top:420px;font-size:8.5px;line-height:15.5px}
.ad--half .badge{left:197px;top:403px;width:80px;height:80px}
.ad--half .footer{height:76px}
.ad--half .footer__contacts{left:27px;top:19px;font-size:8px;line-height:13.5px}
.ad--half .footer__label{width:50px;margin-right:3px;font-size:7px}
.ad--half .footer__label--spaced{letter-spacing:3.5px}
.ad--half .footer__divider{left:186px;top:5px;bottom:5px}
.ad--half .footer__brand{left:197px;top:8px}
.ad--half .footer__regions{font-size:4px;margin-bottom:8px;letter-spacing:.7px}
.ad--half .brand__mark{width:21px;height:21px;margin-right:7px}
.ad--half .brand__name{font-size:16px}
.ad--half .brand__tagline{font-size:3px;margin-top:2px}
.ad--half .footer__url{font-size:6px;letter-spacing:3px;margin-top:9px}
</style>
</head>
<body>

<div class="size-label size-label--full">FULL PAGE</div>
<div class="size-label size-label--half">HALF PAGE</div>

<section class="ad ad--full">
  <div class="ad__art" role="img" aria-label="Illustration of three servers rising out of a cloud with a printed page sliding out"></div>
  <div class="ad__shadow"></div>
  <svg class="ad__link" viewBox="0 0 220 345" aria-hidden="true">
    <path d="M0 4 H190 Q214 4 214 28 V345" fill="none" stroke="#fff" stroke-width="5" stroke-dasharray="5 5"/>
  </svg>
  <div class="ad__arm" role="img" aria-label="Illustration of a hand in a suit sleeve holding up a red smartphone"></div>

  <h2 class="ad__heading">Enterprise SSD cloud with total flexibility</h2>
  <p class="ad__intro">Quickly and cost effectively build Norvix, opalBSD and Quenta servers in the cloud and pay just for what you need.</p>
  <ul class="ad__points">
    <li>24/7/365 support as standard</li>
    <li>Partner with plaventro</li>
    <li>11 Cloud Locations</li>
    <li>Data Protection &amp; Privacy</li>
    <li>Enterprise Platforms with plaventro</li>
  </ul>

  <svg class="badge" viewBox="0 0 142 142" role="img" aria-label="Cloud locations available around the world">
    <defs><clipPath id="badge-clip-full"><circle cx="71" cy="71" r="66"/></clipPath></defs>
    <circle cx="71" cy="71" r="70" fill="#fff"/>
    <g clip-path="url(#badge-clip-full)">
      <polygon points="0,0 142,0 142,76 0,44" fill="#9fd32a"/>
    </g>
    <circle cx="71" cy="71" r="66" fill="none" stroke="#9fd32a" stroke-width="3"/>
    <g transform="rotate(13 71 71)" fill="#475864" font-family="Nunito, sans-serif" text-anchor="middle">
      <text x="71" y="40" font-size="13" font-weight="700">CLOUD</text>
      <text x="71" y="55" font-size="13" font-weight="700">LOCATIONS...</text>
      <text x="71" y="85" font-size="11" font-weight="800" font-style="italic">Available around</text>
      <text x="71" y="99" font-size="11" font-weight="800" font-style="italic">the world!</text>
    </g>
  </svg>

  <footer class="footer">
    <div class="footer__contacts">
      <div class="footer__row"><span class="footer__label footer__label--spaced">Sales:</span><span class="footer__value">sales@plaventro.com</span></div>
      <div class="footer__row"><span class="footer__label">Accounts:</span><span class="footer__value">accounts@plaventro.com</span></div>
      <div class="footer__row"><span class="footer__label">Tech Support:</span><span class="footer__value">support@plaventro.com</span></div>
    </div>
    <div class="footer__divider"></div>
    <div class="footer__brand">
      <div class="footer__regions">UNITED KINGDOM &nbsp;|&nbsp; IRELAND &nbsp;|&nbsp; UNITED STATES</div>
      <div class="brand">
        <span class="brand__mark"></span>
        <div class="brand__text">
          <span class="brand__name">plaventro</span>
          <span class="brand__tagline">The cloud you've been waiting for,<br>might be closer than you think</span>
        </div>
      </div>
      <div class="footer__url">www.plaventro.com</div>
    </div>
  </footer>
</section>

<section class="ad ad--half">
  <div class="ad__art" role="img" aria-label="Illustration of three servers rising out of a cloud with a printed page sliding out"></div>
  <div class="ad__shadow"></div>
  <svg class="ad__link" viewBox="0 0 125 275" aria-hidden="true">
    <path d="M0 3 H106 Q121 3 121 18 V275" fill="none" stroke="#fff" stroke-width="3.5" stroke-dasharray="3.5 3.5"/>
  </svg>
  <div class="ad__arm" role="img" aria-label="Illustration of a hand in a suit sleeve holding up a red smartphone"></div>

  <h2 class="ad__heading">Enterprise SSD cloud<br>with total flexibility</h2>
  <p class="ad__intro">Quickly and cost effectively build Norvix, opalBSD and Quenta servers in the cloud and pay just for what you need.</p>
  <ul class="ad__points">
    <li>24/7/365 support as standard</li>
    <li>Partner with plaventro</li>
    <li>11 Cloud Locations</li>
    <li>Data Protection &amp; Privacy</li>
    <li>Enterprise Platforms with plaventro</li>
  </ul>

  <svg class="badge" viewBox="0 0 142 142" role="img" aria-label="Cloud locations available around the world">
    <defs><clipPath id="badge-clip-half"><circle cx="71" cy="71" r="66"/></clipPath></defs>
    <circle cx="71" cy="71" r="70" fill="#fff"/>
    <g clip-path="url(#badge-clip-half)">
      <polygon points="0,0 142,0 142,76 0,44" fill="#9fd32a"/>
    </g>
    <circle cx="71" cy="71" r="66" fill="none" stroke="#9fd32a" stroke-width="3"/>
    <g transform="rotate(13 71 71)" fill="#475864" font-family="Nunito, sans-serif" text-anchor="middle">
      <text x="71" y="40" font-size="13" font-weight="700">CLOUD</text>
      <text x="71" y="55" font-size="13" font-weight="700">LOCATIONS...</text>
      <text x="71" y="85" font-size="11" font-weight="800" font-style="italic">Available around</text>
      <text x="71" y="99" font-size="11" font-weight="800" font-style="italic">the world!</text>
    </g>
  </svg>

  <footer class="footer">
    <div class="footer__contacts">
      <div class="footer__row"><span class="footer__label footer__label--spaced">Sales:</span><span class="footer__value">sales@plaventro.com</span></div>
      <div class="footer__row"><span class="footer__label">Accounts:</span><span class="footer__value">accounts@plaventro.com</span></div>
      <div class="footer__row"><span class="footer__label">Tech Support:</span><span class="footer__value">support@plaventro.com</span></div>
    </div>
    <div class="footer__divider"></div>
    <div class="footer__brand">
      <div class="footer__regions">UNITED KINGDOM | IRELAND | UNITED STATES</div>
      <div class="brand">
        <span class="brand__mark"></span>
        <div class="brand__text">
          <span class="brand__name">plaventro</span>
          <span class="brand__tagline">The cloud you've been waiting for,<br>might be closer than you think</span>
        </div>
      </div>
      <div class="footer__url">www.plaventro.com</div>
    </div>
  </footer>
</section>

</body>
</html>
```